Redesign Business Cards, Attached

Please read instructions carefully. If you have any questions send a message before submitting your ONE design. Please redesign attached business cards. Double sided. Use same content and descriptions. Use black, silver, crimson red and gold colors. My only issue with the attached design is the background colors. I like the layout as-is. I can provide the individual pictures on the back side later. Do not submit more than one design. One submission shall include both front and back. Do not submit front and back separately. A second project will be launched to create a matching post card after completion of this.
Industry/Entity Type
see description and attachments.
Contact Information for Business Card
Requirements
Must have
- see description and attachments.
Nice to have
Should not have

```html
<!DOCTYPE html>
<html lang="en">
<head>
<meta charset="utf-8">
<title>Harlow Helm Training – Business Card</title>
<link href="https://fonts.googleapis.com/css2?family=Arimo:wght@400;700&family=Questrial&display=swap" rel="stylesheet">
<style>
  :root {
    --page: #ffffff;
    --card-dark: #332b29;
    --card-light: #efefef;
    --crimson: #c8262f;
    --gold: #d9b24a;
    --gold-deep: #b58a22;
    --silver-light: #f2f2f2;
    --silver-mid: #d3d5d4;
    --ink: #2b2b2b;
    --white: #f4f4f4;
    --black: #141414;
  }
  * { margin: 0; padding: 0; box-sizing: border-box; }
  html, body { width: 1200px; height: 664px; overflow: hidden; background: var(--page); }
  .sheet { position: relative; width: 1200px; height: 664px; }
  .card { position: absolute; top: 190px; width: 461px; height: 264px; overflow: hidden; }

  /* Front */
  .card-front { left: 92px; background: var(--card-dark); color: var(--white); text-align: center; }
  .brand-mark { position: absolute; top: 34px; left: 0; right: 0; display: flex; align-items: center; justify-content: center; gap: 10px; }
  .brand-dot { width: 46px; height: 46px; border-radius: 50%; background: var(--gold); }
  .brand-name { font-family: "Arimo", sans-serif; font-weight: 700; font-size: 15px; letter-spacing: 1px; color: var(--gold); text-align: left; line-height: 1.2; }
  .holder-name { position: absolute; top: 118px; left: 0; right: 0; font-family: "Arimo", sans-serif; font-weight: 700; font-size: 27px; letter-spacing: .3px; color: var(--white); }
  .holder-title { position: absolute; top: 149px; left: 0; right: 0; font-family: "Questrial", sans-serif; font-size: 14.5px; line-height: 16px; letter-spacing: .6px; color: var(--white); }
  .divider { position: absolute; top: 189px; left: 134px; width: 194px; height: 1px; background: var(--crimson); }
  .phone-line { position: absolute; top: 192px; left: 0; right: 0; display: flex; align-items: center; justify-content: center; gap: 4px; font-family: "Arimo", sans-serif; font-weight: 700; font-size: 19px; letter-spacing: 1px; color: var(--crimson); }
  .phone-icon { width: 16px; height: 16px; }
  .contact-row { position: absolute; top: 218px; left: 0; right: 0; display: flex; justify-content: center; gap: 17px; font-family: "Questrial", sans-serif; font-size: 9.5px; letter-spacing: .4px; color: var(--white); }
  .contact-item { display: flex; align-items: center; gap: 4px; }
  .contact-item svg { width: 9px; height: 9px; }

  /* Back */
  .card-back { left: 615px; background: var(--card-light); color: var(--ink); }
  .accent-band { position: absolute; left: 0; top: 38px; width: 38px; height: 133px; background: var(--crimson); }
  .service-list { position: absolute; left: 54px; top: 34px; list-style: none; font-family: "Arimo", sans-serif; font-size: 12.6px; line-height: 17.7px; color: var(--ink); }
  .back-mark { position: absolute; left: 334px; top: 38px; width: 96px; text-align: center; }
  .back-dot { width: 86px; height: 86px; margin: 0 auto; border-radius: 50%; background: var(--black); border: 3px solid var(--gold); }
  .back-name { margin-top: 5px; font-family: "Arimo", sans-serif; font-weight: 700; font-size: 9px; letter-spacing: .5px; color: var(--black); }
  .silver-band { position: absolute; left: 0; bottom: 0; width: 100%; height: 39px;
    background: linear-gradient(90deg, var(--silver-mid) 0%, var(--silver-light) 15%, var(--silver-mid) 45%, var(--silver-light) 75%, var(--silver-mid) 100%); }
  .back-url { position: absolute; left: 54px; top: 231px; font-family: "Arimo", sans-serif; font-weight: 700; font-size: 15px; letter-spacing: 1.2px; color: var(--ink); }
  .yacht-art { position: absolute; left: 242px; top: 190px; width: 200px; height: 62px;
    background: linear-gradient(180deg, rgba(220,222,221,.0) 0%, rgba(205,207,206,.7) 100%); border-radius: 4px; }
</style>
</head>
<body>
<main class="sheet">
  <section class="card card-front" aria-label="Card front">
    <div class="brand-mark">
      <span class="brand-dot"></span>
      <span class="brand-name">HARLOW HELM<br>TRAINING</span>
    </div>
    <h1 class="holder-name">DANIEL R. HARLOW</h1>
    <p class="holder-title">USCG Licensed Captain<br>Certified instructor</p>
    <div class="divider"></div>
    <p class="phone-line">
      <span>TEXT</span>
      <svg class="phone-icon" viewBox="0 0 16 16" aria-hidden="true">
        <rect width="16" height="16" rx="3" fill="var(--crimson)"/>
        <path d="M5 3.5l2 2.2-1 1.2c.6 1.4 1.6 2.4 3 3l1.2-1 2.2 2-1.2 1.6C7.5 12.3 3.7 8.5 3.5 4.7z" fill="var(--card-dark)"/>
      </svg>
      <span>(555)014-2290</span>
    </p>
    <div class="contact-row">
      <span class="contact-item">
        <svg viewBox="0 0 10 10" aria-hidden="true"><rect x=".5" y="1.5" width="9" height="7" fill="none" stroke="currentColor"/><path d="M.5 1.5L5 5.5l4.5-4" fill="none" stroke="currentColor"/></svg>
        hello@helmlesson.com
      </span>
      <span class="contact-item">
        <svg viewBox="0 0 10 10" aria-hidden="true"><circle cx="5" cy="5" r="4.4" fill="none" stroke="currentColor" stroke-width=".8"/><ellipse cx="5" cy="5" rx="2" ry="4.4" fill="none" stroke="currentColor" stroke-width=".8"/><path d="M.6 5h8.8M1.3 3h7.4M1.3 7h7.4" stroke="currentColor" stroke-width=".7"/></svg>
        www.HelmLesson.com
      </span>
    </div>
  </section>

  <section class="card card-back" aria-label="Card back">
    <div class="accent-band" role="img" aria-label="Anchor with coiled rope illustration on crimson band"></div>
    <ul class="service-list">
      <li>Hands-On Boat Training</li>
      <li>Introduction to Power boating</li>
      <li>Precision Docking &amp; Boat Handling</li>
      <li>Open Water Boat Handling</li>
      <li>Island Anchoring</li>
      <li>Open Water Advanced Maneuvers</li>
      <li>Coastal Navigation</li>
      <li>Captaining/ Piloting Service for Your Outings</li>
    </ul>
    <div class="back-mark">
      <div class="back-dot"></div>
      <p class="back-name">HARLOW HELM TRAINING</p>
    </div>
    <div class="silver-band"></div>
    <p class="back-url">www.HelmLesson.com</p>
    <div class="yacht-art" role="img" aria-label="Silver line drawing of a motor yacht"></div>
  </section>
</main>
</body>
</html>
```